HARBOUR LANE DECOR

We need a web design for a new business based in Bonny Hills (NSW). We are a small retail outlet on the Mid North Coast (NSW, Australia) selling home wares, gifts, beach wear, artwork, and hampers etc. We would like to a few different samples if that's not too much trouble (e.g. black and white vs colour, e.g. "beach colours").
We would like the website to communicate that we are an affordable, local (community based) business, with customer satisfaction at the forefront of our mind. We have a strong customer service focus, and in addition to retail sales we are now looking to expand into the online hamper business.
We are open 7 days (except public holidays).
Note: We like the design / layout of the "Cork Pail 'N' Shelf Website" if you would like to compare www.corkpailnshelf.com.au

Industry/Entity Type

Business

```html
<!DOCTYPE html>
<html lang="en">
<head>
<meta charset="utf-8">
<title>Harbour Lane Decor</title>
<link rel="stylesheet" href="https://fonts.googleapis.com/css2?family=Source+Sans+3:ital,wght@0,400;0,600;1,400&family=Playfair+Display:wght@400&family=Delius&display=swap">
<style>
:root{
  --black:#000;
  --white:#fff;
  --ink:#333;
  --muted:#666;
  --rule:#d9d9d9;
  --teal:#6ed9d2;
  --green:#c5e0a5;
  --blue:#c9e3ea;
  --yellow:#fdd26e;
  --pink:#f4c9d3;
  --grey-tile:#dedcdd;
  --accent-pink:#f06f95;
  --photo-light:#d4d4d4;
  --photo-dark:#6b6b6b;
}
*{box-sizing:border-box;margin:0;padding:0}
html,body{width:791px;height:1200px;overflow:hidden;background:var(--white)}
body{position:relative;font-family:"Source Sans 3","Source Sans Pro",sans-serif;color:var(--ink)}
.abs{position:absolute}
.photo{background:linear-gradient(135deg,var(--photo-light),var(--photo-dark))}

/* header */
.site-header{left:0;top:0;width:791px;height:50px;background:var(--black)}
.ornament{top:0;height:50px;background:radial-gradient(circle at 40% 50%,#5a5a5a,#111 70%)}
.ornament-left{left:0;width:90px}
.ornament-right{left:710px;width:81px}
.brand{left:121px;top:16px;color:var(--white);font-size:15px;font-weight:400;white-space:nowrap}
.login{left:598px;top:10px;width:72px;height:14px;border-radius:7px;background:var(--white);font-size:7px;text-align:center;line-height:14px;color:var(--black);white-space:nowrap}
.nav span{position:absolute;top:36px;font-size:7.5px;color:var(--white);white-space:nowrap}
.nav span.active{color:var(--teal)}
.nav-dot{left:367px;top:47px;width:6px;height:3px;border-radius:3px 3px 0 0;background:var(--teal)}

/* hero */
.tiles{left:121px;top:66px;width:240px;height:219px;display:grid;grid-template-columns:repeat(3,1fr);grid-template-rows:repeat(3,1fr);gap:1px;background:var(--white)}
.tile{display:flex;align-items:center;justify-content:center;text-align:center;color:var(--white);font-size:10.5px;line-height:1.3;background:var(--grey-tile)}
.tile-green{background:var(--green)}
.tile-blue{background:var(--blue)}
.tile-teal{background:var(--teal)}
.tile-yellow{background:var(--yellow)}
.tile-pink{background:var(--pink)}
.slider{left:361px;top:66px;width:309px;height:219px;background:linear-gradient(160deg,#e9e9e9,#8a8a8a 55%,#3e3e3e)}
.slide-title{left:361px;top:108px;width:309px;text-align:center;font-family:"Playfair Display",Georgia,serif;font-weight:400;color:var(--teal);font-size:24px;line-height:44px;white-space:nowrap}
.arrow{top:165px;width:14px;height:20px;background:var(--black)}
.dots{left:502px;top:273px;display:flex;gap:4px}
.dots i{width:4px;height:4px;border-radius:50%;background:var(--white)}
.dots i.on{background:var(--teal)}
.intro{left:0;top:294px;width:791px;text-align:center;font-size:9.5px;line-height:16px;color:#444}
.contact-bar{left:121px;top:334px;width:549px;height:20px;background:var(--black);color:var(--white);font-size:11.5px;display:flex;align-items:center;justify-content:center;gap:11px;white-space:nowrap}
.contact-bar span{display:flex;align-items:center;gap:5px}

.rule-h{left:0;top:389px;width:791px;height:1px;background:var(--rule)}
.rule-v{left:281px;top:389px;width:1px;height:739px;background:var(--rule)}

/* sidebar */
.owners{left:121px;top:419px;width:141px;height:108px}
.owners-title{left:121px;top:535px;font-family:"Delius",cursive;font-weight:400;font-size:12.5px;color:var(--accent-pink)}
.owners-text{left:121px;top:559px;width:141px;font-size:6.8px;line-height:12.8px;color:var(--muted)}
.dotted{left:121px;width:141px;border-top:1px dotted #999}
.signup-title{left:121px;top:690px;font-size:12px;font-weight:400;color:var(--ink)}
.signup-sub{left:121px;top:705px;font-size:8.5px;font-style:italic;color:var(--teal)}
.field{left:121px;width:141px;height:17px;border:1px solid #ccc;font-size:4.5px;color:#aaa;padding:6px 3px}
.btn-send{left:211px;top:780px;width:51px;height:13px;background:var(--teal);color:var(--white);font-size:8px;text-align:center;line-height:13px}
.search-field{left:121px;top:852px;width:90px;height:17px;border:1px solid #ccc}
.btn-search{left:211px;top:852px;width:51px;height:17px;background:var(--black);color:var(--white);font-size:8px;text-align:center;line-height:17px}

/* category cards */
.card{left:300px;width:370px;height:151px}
.card .pic{position:absolute;top:0;height:151px;width:312px}
.card .band{position:absolute;top:0;width:58px;height:151px}
.card-right .pic{left:0}.card-right .band{left:312px}
.card-left .pic{left:58px}.card-left .band{left:0}
.band-label{position:absolute;left:0;top:8px;width:58px;height:118px;display:flex;align-items:center;justify-content:center;writing-mode:vertical-rl;transform:rotate(180deg);font-family:"Playfair Display",Georgia,serif;font-weight:400;font-size:19px;color:var(--black);white-space:nowrap}
.browse{position:absolute;bottom:10px;left:10px;width:37px;height:11px;border-radius:2px;background:var(--white);font-size:5.5px;text-align:center;line-height:11px;color:var(--black);white-space:nowrap}

/* footer */
.to-top{left:741px;top:1156px;width:25px;height:25px;border-radius:3px;background:#ddd;display:flex;align-items:center;justify-content:center}
.site-footer{left:0;top:1168px;width:791px;height:32px;background:var(--black);color:var(--white);font-size:7.5px}
.footer-links{position:absolute;left:121px;top:0;height:32px;display:flex;align-items:center;gap:10px;white-space:nowrap}
.footer-links span{color:var(--white)}
.social{width:16px;height:16px;border:1px solid var(--white);border-radius:50%;display:flex;align-items:center;justify-content:center}
.copyright{position:absolute;right:121px;top:13px;font-size:5.5px;white-space:nowrap}
</style>
</head>
<body>

<header class="abs site-header">
  <div class="abs ornament ornament-left" role="img" aria-label="Decorative white swirl flourish"></div>
  <div class="abs ornament ornament-right" role="img" aria-label="Decorative white swirl flourish"></div>
  <div class="abs brand">Harbour Lane Decor</div>
  <div class="abs login">Log in &nbsp;/&nbsp; Register</div>
  <svg class="abs" style="left:365px;top:23px" width="11" height="10" viewBox="0 0 11 10" fill="none" stroke="#6ed9d2" stroke-width="1"><rect x="1" y="3.5" width="9" height="6"/><line x1="5.5" y1="3.5" x2="5.5" y2="9.5"/><path d="M5.5 3.5C3 0 1.5 2 3 3.5M5.5 3.5C8 0 9.5 2 8 3.5"/></svg>
  <nav class="nav">
    <span class="active" style="left:361px">Home</span>
    <span style="left:402px">Home ware</span>
    <span style="left:461px">Kitchen ware</span>
    <span style="left:525px">Linen</span>
    <span style="left:564px">Gifts</span>
    <span style="left:600px">Contact Us</span>
  </nav>
  <svg class="abs" style="left:657px;top:33px" width="13" height="11" viewBox="0 0 13 11" fill="none" stroke="#fff" stroke-width="1"><path d="M0 1h2.5l2 6h6.5l1.5-4.5H3.5"/><circle cx="5.5" cy="9.3" r="1"/><circle cx="10" cy="9.3" r="1"/></svg>
  <div class="abs nav-dot"></div>
</header>

<section>
  <div class="abs tiles">
    <div class="tile tile-green">HOME WARE</div>
    <div class="tile"></div>
    <div class="tile tile-blue">LINEN</div>
    <div class="tile"></div>
    <div class="tile tile-teal">
      <svg width="26" height="22" viewBox="0 0 26 22" fill="#fff"><path d="M13 0L0 11h3v11h7v-7h6v7h7V11h3z"/></svg>
    </div>
    <div class="tile"></div>
    <div class="tile tile-yellow">KITCHEN<br>WARE</div>
    <div class="tile"></div>
    <div class="tile tile-pink">GIFTS</div>
  </div>
  <div class="abs slider" role="img" aria-label="Shop interior with shelves of cushions, homewares and gifts"></div>
  <h1 class="abs slide-title">Colourful inspiration<br>for your<br>home or gift ideas</h1>
  <div class="abs arrow" style="left:361px"><svg width="14" height="20" viewBox="0 0 14 20" fill="none" stroke="#fff" stroke-width="1.5"><path d="M9 6l-4 4 4 4"/></svg></div>
  <div class="abs arrow" style="left:656px"><svg width="14" height="20" viewBox="0 0 14 20" fill="none" stroke="#fff" stroke-width="1.5"><path d="M5 6l4 4-4 4"/></svg></div>
  <div class="abs dots"><i></i><i class="on"></i><i></i><i></i></div>

  <p class="abs intro">Harbour Lane Decor supplying quality and affordable home ware, kitchen ware, linen and gifts to the beautiful Bonny Hills and surrounding areas.<br>We open 7 days a week from 9am - 4pm (except public holidays)</p>

  <div class="abs contact-bar">
    <span><svg width="7" height="10" viewBox="0 0 7 10" fill="none" stroke="#fff" stroke-width="1"><path d="M3.5 9.5S.5 6 .5 3.5a3 3 0 016 0C6.5 6 3.5 9.5 3.5 9.5z"/><circle cx="3.5" cy="3.5" r="1"/></svg>7/22 Tidewater Crescent, Bonny Hills, Port Macquarie, New South Wales</span>
    <span><svg width="9" height="9" viewBox="0 0 9 9" fill="#fff"><path d="M1.8 0L3.5 2.2 2.6 3.4a5 5 0 003 3l1.2-.9L9 7.2 7.6 9C3.6 8.7.3 5.4 0 1.4z"/></svg>0412558190, 0438671402</span>
  </div>
</section>

<div class="abs rule-h"></div>
<div class="abs rule-v"></div>

<aside>
  <div class="abs owners photo" role="img" aria-label="The two shop owners standing in their store"></div>
  <h2 class="abs owners-title">meet anna &amp; beth</h2>
  <p class="abs owners-text">Lorem ipsum dolor sit amet, consectetur adipisci eiusmod tempor incididunt ut labore et dolore. Ut enimad minim veniam, quis nostrud exercitati nisi ut aliquip ex ea commo do consequat. Duis u reprehenderit in voluptate velit esse cillum dolor pariat. &nbsp;Excepteur sint occaecat cupidatat non, culpa qui officia deserunt mollit anim idest.</p>
  <div class="abs dotted" style="top:669px"></div>
  <h3 class="abs signup-title">SIGN-UP</h3>
  <div class="abs signup-sub">for our email updates</div>
  <div class="abs field" style="top:727px">NAME</div>
  <div class="abs field" style="top:753px">EMAIL</div>
  <div class="abs btn-send">SEND</div>
  <div class="abs dotted" style="top:824px"></div>
  <div class="abs search-field"></div>
  <div class="abs btn-search">SEARCH</div>
  <div class="abs dotted" style="top:901px"></div>
</aside>

<main>
  <div class="abs card card-right" style="top:419px">
    <div class="pic photo" role="img" aria-label="Patterned ceramic bowls, plates and jugs on a table"></div>
    <div class="band" style="background:var(--green)"><div class="band-label">home ware</div><div class="browse">Browse All</div></div>
  </div>
  <div class="abs card card-left" style="top:605px">
    <div class="pic photo" role="img" aria-label="Saucepans, glassware and baking dishes on display"></div>
    <div class="band" style="background:var(--yellow)"><div class="band-label">kitchen ware</div><div class="browse">Browse All</div></div>
  </div>
  <div class="abs card card-right" style="top:791px">
    <div class="pic photo" role="img" aria-label="Patterned cushions and folded linen on shelves"></div>
    <div class="band" style="background:var(--blue)"><div class="band-label">linen</div><div class="browse">Browse All</div></div>
  </div>
  <div class="abs card card-left" style="top:977px">
    <div class="pic photo" role="img" aria-label="Shelving cubes filled with mugs, candles and gift items"></div>
    <div class="band" style="background:var(--pink)"><div class="band-label">gifts</div><div class="browse">Browse All</div></div>
  </div>
</main>

<div class="abs to-top"><svg width="10" height="6" viewBox="0 0 10 6" fill="none" stroke="#333" stroke-width="1.5"><path d="M1 5l4-4 4 4"/></svg></div>

<footer class="abs site-footer">
  <div class="footer-links">
    <span>Contact Us</span><span>|</span><span>About Us</span><span>|</span><span>Terms and Conditions</span><span>|</span><span>Follow Us On:</span>
    <span class="social" role="img" aria-label="Share on social media"><svg width="9" height="9" viewBox="0 0 9 9" fill="#fff" stroke="#fff" stroke-width=".8"><circle cx="7" cy="1.8" r="1.3"/><circle cx="2" cy="4.5" r="1.3"/><circle cx="7" cy="7.2" r="1.3"/><path d="M2 4.5L7 1.8M2 4.5L7 7.2" fill="none"/></svg></span>
  </div>
  <div class="copyright">© 2015 Harbour Lane Decor. All Rights Reserved.</div>
</footer>

</body>
</html>
```